Book Cover for Notes on the Quiet River's Far Lamps

I need a book cover for a 6 x 9 paperback titled Notes on the Quiet River's Far Lamps Gathered by Sailors and Weavers Resting in the Valley beyond the Northern Valley. It has to do with consciousness, the mind, incarnation onto Earth, leaving Earth, and the life in the life after this life. I have an idea I'm providing with this description, but I am open to anything that would be striking and stimulating, whether with a book or not. I am the author, T. Warren Blakely. I've added another background idea to see if anyone can do something with it and I've increased the budget.

```html
<!DOCTYPE html>
<html lang="en">
<head>
<meta charset="utf-8">
<title>Notes on the Quiet River's Far Lamps — Book Cover</title>
<link rel="stylesheet" href="https://fonts.googleapis.com/css2?family=Marcellus&display=swap">
<style>
  :root {
    --stage: #8a3a1e;
    --cover-dark: #1c140e;
    --cover-mid: #5a4128;
    --beam-gold: #d9b676;
    --page-gold: #e2bd7c;
    --page-shade: #a8773f;
    --floor: #6b4427;
    --floor-light: #7d5230;
    --ink: #fbf6ec;
  }
  * { margin: 0; padding: 0; box-sizing: border-box; }
  html, body {
    width: 1200px;
    height: 601px;
    overflow: hidden;
    background: var(--stage);
  }
  .stage {
    position: relative;
    width: 1200px;
    height: 601px;
  }
  .cover {
    position: absolute;
    left: 400px;
    top: 0;
    width: 401px;
    height: 601px;
    overflow: hidden;
    background: var(--cover-dark);
    font-family: "Marcellus", serif;
    color: var(--ink);
    text-align: center;
  }
  .cover-backdrop {
    position: absolute;
    inset: 0;
    background:
      radial-gradient(ellipse 36% 60% at 50% 22%, rgba(217,182,118,0.7), rgba(217,182,118,0) 100%),
      linear-gradient(180deg, var(--cover-dark) 0%, var(--cover-mid) 42%, #3d2a19 72%, var(--floor) 80%, var(--floor-light) 100%);
  }
  .cover-backdrop::after {
    content: "";
    position: absolute;
    inset: 0;
    background: linear-gradient(90deg, rgba(10,7,4,0.75) 0%, rgba(10,7,4,0) 28%, rgba(10,7,4,0) 72%, rgba(10,7,4,0.75) 100%);
  }
  .book-art {
    position: absolute;
    left: 8px;
    top: 347px;
    width: 392px;
    height: 130px;
    border-radius: 40% 40% 4px 4px / 60% 60% 4px 4px;
    background:
      radial-gradient(ellipse 50% 70% at 50% 60%, var(--page-gold) 0%, var(--page-shade) 70%, rgba(120,80,40,0.9) 100%);
  }
  .title {
    position: absolute;
    top: 95px;
    left: 0;
    width: 100%;
    font-weight: 400;
    font-size: 33px;
    line-height: 38px;
    letter-spacing: 0.2px;
    text-transform: uppercase;
  }
  .subtitle {
    position: absolute;
    top: 174px;
    left: 0;
    width: 100%;
    text-transform: uppercase;
    letter-spacing: 1.2px;
  }
  .subtitle-lead {
    display: block;
    font-size: 11.5px;
    line-height: 17px;
  }
  .subtitle-body {
    display: block;
    font-size: 13.5px;
    line-height: 17.5px;
  }
  .author {
    position: absolute;
    bottom: 18px;
    left: 0;
    width: 100%;
    font-size: 15px;
    letter-spacing: 0.6px;
    text-transform: uppercase;
  }
</style>
</head>
<body>
  <main class="stage">
    <section class="cover">
      <div class="cover-backdrop"></div>
      <div class="book-art" role="img" aria-label="Open old book with curling golden pages resting on a wooden surface, lit by warm beams of light falling from above"></div>
      <h1 class="title">Notes on the Quiet<br>River's Far Lamps</h1>
      <p class="subtitle">
        <span class="subtitle-lead">Gathered by</span>
        <span class="subtitle-body">Sailors and Weavers</span>
        <span class="subtitle-body">Resting in the Valley beyond</span>
        <span class="subtitle-body">the Northern Valley</span>
      </p>
      <p class="author">T. Warren Blakely</p>
    </section>
  </main>
</body>
</html>
```